依頼詳細
会社の名刺デザインを新しくします。
中核になる3つの事業にそれぞれスタッフがいますが、名刺は共通のものを使用したいと考えています。
スタイリッシュかつ遊び心があって、もらった人が目を引くような名刺にしたいです。
あえてカラーなど希望イメージの指定は致しませんので、多種多様のデザインを見て決めたいと思います。
会社ロゴを添付します。カラーは自由に変更していただいて構いません。
記載項目
表面:社名、事業名、肩書き、名前、連絡先(住所、TEL、FAX、メール等)
裏面:事業内容、プロフィールなど
希望イメージ
シンプル 複雑
単色 カラフル
暗い 明るい
日常 高級
遊び心 厳粛
未来的 伝統的
女性的 男性的
希望する色
設定なし
納品ファイル
設定なし
補足説明
設定なし
縦型、横型、二つ折り名刺、顔写真入りなども特に定めませんので、自由にご提案いただけると選びがいがあり有り難いです。
当選報酬の金額引き上げと選定確約について変更致しました。
よろしくお願い致します。
会社ロゴを添付しました。
ランサーの皆様、たくさんの提案ありがとうございます。
様々な提案を見た結果イメージが固まってきましたので、締め切りを延長して修正等をしていただけないかと思います。

【追記内容】
・事業所名が和風なので、和風な感じが合いそう。
・事業所名の「楓庵の里」は筆文字にしたらいいのではないか?
・匠な感じが出るといい。(白と黒を基調にするとどうなるでしょう?他の色でも構えいません。)
■ 選んだ理由

社員全員による投票にて決定いたしましたので、万人受けしやすいデザインだったのではないかと思います。また、修正等に幾度も迅速に対応していただいた点もよかったです。

■ 提案者全員のお礼・コメント

70を超すランサーの方々から100を超える提案を頂き誠にありがとうございました。当選作品以外にも素晴らしいデザインが多く、選定するのも大変でした。ありがとうございました。

```html
<!DOCTYPE html>
<html lang="ja">
<head>
<meta charset="utf-8">
<title>楓庵の里 名刺 裏面</title>
<link href="https://fonts.googleapis.com/css2?family=Noto+Sans+JP:wght@400;500&family=Yuji+Syuku&display=swap" rel="stylesheet">
<style>
  :root{
    --paper:#ffffff;
    --ink:#3b322c;
    --brown:#8a7464;
    --strip:#d8cec1;
    --strip-deep:#b9a998;
    --box-line:#6a5a4e;
  }
  *{margin:0;padding:0;box-sizing:border-box}
  html,body{width:726px;height:1200px;overflow:hidden;background:var(--paper)}
  .card{position:relative;width:726px;height:1200px;background:var(--paper);color:var(--ink);
    font-family:"Noto Sans JP",sans-serif}
  .side-pattern{position:absolute;top:0;right:0;width:121px;height:1200px;
    background:linear-gradient(180deg,var(--strip) 0%,var(--strip-deep) 55%,var(--strip) 100%)}
  .brand{position:absolute;top:28px;left:0;width:605px;text-align:center}
  .brand-mark{display:block;width:86px;height:86px;margin:0 auto 10px;border-radius:50%;background:var(--brown)}
  .brand-name{font-size:22px;font-weight:500;color:var(--brown);letter-spacing:.08em}
  .services{position:absolute;top:238px;left:66px;list-style:none;font-size:21px;line-height:30px;color:var(--ink)}
  .services li{display:flex;align-items:center;gap:8px}
  .services svg{flex:none}
  .office-name{position:absolute;top:255px;left:395px;font-family:"Yuji Syuku",serif;font-size:54px;color:var(--ink);letter-spacing:.04em}
  .section{position:absolute;left:0;width:605px;text-align:center}
  .section h2{font-size:27px;font-weight:500;letter-spacing:.04em}
  .business{top:465px}
  .business ul{list-style:none;margin-top:20px;font-size:30px;line-height:38px}
  .profile{top:745px}
  .box-rows{margin-top:20px;display:flex;flex-direction:column;align-items:center;gap:10px}
  .business .box-rows{margin-top:12px}
  .box-row{display:flex;gap:5px}
  .box-row span{width:22px;height:22px;border:2px solid var(--box-line)}
  .arrow{position:absolute;top:1005px;left:190px}
  .tagline{position:absolute;top:1097px;left:0;width:605px;text-align:center;font-size:21px;letter-spacing:.02em}
</style>
</head>
<body>
<div class="card">
  <div class="side-pattern" role="img" aria-label="縦に伸びる細い枝の和風パターン"></div>

  <div class="brand">
    <span class="brand-mark"></span>
    <span class="brand-name">kaede works</span>
  </div>

  <ul class="services">
    <li><svg width="20" height="20" viewBox="0 0 20 20"><rect x="1" y="1" width="18" height="18" fill="none" stroke="#6a5a4e" stroke-width="2"/><path d="M4 10l4 4 9-11" fill="none" stroke="#3b322c" stroke-width="2.2"/></svg>デイサービス</li>
    <li><svg width="20" height="20" viewBox="0 0 20 20"><rect x="1" y="1" width="18" height="18" fill="none" stroke="#6a5a4e" stroke-width="2"/></svg>訪問看護ステーション</li>
    <li><svg width="20" height="20" viewBox="0 0 20 20"><rect x="1" y="1" width="18" height="18" fill="none" stroke="#6a5a4e" stroke-width="2"/></svg>居宅介護支援センター</li>
  </ul>
  <div class="office-name">楓庵の里</div>

  <section class="section business">
    <h2>事業内容</h2>
    <ul>
      <li>デイサービス</li>
      <li>訪問看護ステーション</li>
      <li>居宅介護支援事業所</li>
    </ul>
    <div class="box-rows">
      <div class="box-row"><span></span><span></span><span></span><span></span><span></span><span></span><span></span><span></span><span></span><span></span></div>
      <div class="box-row"><span></span><span></span><span></span><span></span><span></span><span></span><span></span><span></span><span></span><span></span></div>
    </div>
  </section>

  <section class="section profile">
    <h2>プロフィール</h2>
    <div class="box-rows">
      <div class="box-row"><span></span><span></span><span></span><span></span><span></span><span></span><span></span><span></span><span></span><span></span></div>
      <div class="box-row"><span></span><span></span><span></span><span></span><span></span><span></span><span></span><span></span><span></span><span></span></div>
      <div class="box-row"><span></span><span></span><span></span><span></span><span></span><span></span><span></span><span></span><span></span><span></span></div>
      <div class="box-row"><span></span><span></span><span></span><span></span><span></span><span></span><span></span><span></span><span></span><span></span></div>
    </div>
  </section>

  <svg class="arrow" width="260" height="30" viewBox="0 0 260 30">
    <path d="M2 22 Q130 20 255 24" fill="none" stroke="#8a7464" stroke-width="2"/>
    <path d="M225 6 L255 24" fill="none" stroke="#8a7464" stroke-width="2"/>
  </svg>

  <p class="tagline">よりよい介護でよりよい生活を</p>
</div>
</body>
</html>
```